Delegate Welcome sign

The Copperfield Lodge hotel in Pine Bush NY is welcoming delegations from many different countries during 2019. We want to make a welcome sign about 16:9 ratio about 4 feet high with raised letters. I have attached a background design that we liked and a template with the wording. As you will see I need help with it.

```html
<!DOCTYPE html>
<html lang="en">
<head>
<meta charset="utf-8">
<title>Copperfield Lodge – Delegate Welcome Sign</title>
<link rel="stylesheet" href="https://fonts.googleapis.com/css2?family=Marcellus&family=Fraunces:wght@700&display=swap">
<style>
  :root {
    --page: #ffffff;
    --forest-dark: #354b42;
    --forest-mid: #4a6a5e;
    --plaque-light: #5b8273;
    --plaque-dark: #2f463d;
    --gold-light: #fff2b8;
    --gold: #d9ae4e;
    --gold-deep: #a97a22;
    --cream: #f6efd2;
  }
  html, body {
    margin: 0;
    padding: 0;
    width: 1200px;
    height: 1000px;
    overflow: hidden;
    background: var(--page);
  }
  .canvas {
    position: relative;
    width: 1200px;
    height: 1000px;
  }
  .welcome-sign {
    position: absolute;
    left: 251px;
    top: 299px;
    width: 698px;
    height: 402px;
    overflow: hidden;
  }
  .leaf-pattern {
    position: absolute;
    inset: 0;
    background:
      radial-gradient(ellipse at 50% 50%, var(--forest-mid) 0%, var(--forest-dark) 75%);
  }
  .plaque-frame {
    position: absolute;
    left: 0;
    top: 0;
    width: 698px;
    height: 402px;
  }
  .plaque-text {
    position: absolute;
    left: 112px;
    width: 474px;
    margin: 0;
    text-align: center;
    color: var(--cream);
    font-family: "Marcellus", serif;
    line-height: 1;
    text-shadow: 0 1px 2px rgba(0, 0, 0, 0.45);
  }
  .line-host { top: 126px; font-size: 21px; }
  .line-welcomes { top: 150px; font-size: 21px; }
  .line-headline {
    top: 188px;
    font-family: "Fraunces", serif;
    font-weight: 700;
    font-size: 25px;
    color: var(--gold);
    transform: rotate(1.8deg);
    text-shadow: 0 1px 1px rgba(0, 0, 0, 0.6);
  }
  .line-place { top: 220px; font-size: 21px; }
  .line-state { top: 243px; font-size: 21px; }
  .line-hashtag {
    top: 273px;
    font-size: 12px;
    color: var(--gold);
  }
</style>
</head>
<body>
<main class="canvas">
  <section class="welcome-sign">
    <div class="leaf-pattern" role="img" aria-label="Background pattern of green leaves bearing the word welcome in many languages"></div>

    <svg class="plaque-frame" viewBox="0 0 698 402" aria-hidden="true">
      <defs>
        <linearGradient id="plaque-fill" x1="0" y1="0" x2="1" y2="1">
          <stop offset="0" stop-color="var(--plaque-light)"/>
          <stop offset="1" stop-color="var(--plaque-dark)"/>
        </linearGradient>
        <linearGradient id="gold-edge" x1="0" y1="0" x2="1" y2="1">
          <stop offset="0" stop-color="var(--gold-light)"/>
          <stop offset="0.45" stop-color="var(--gold)"/>
          <stop offset="1" stop-color="var(--gold-deep)"/>
        </linearGradient>
      </defs>
      <path d="M124,114 L574,114 A12,12 0 0 0 586,126 L586,262 A12,12 0 0 0 574,274 L479,274 C440,302 260,302 221,274 L124,274 A12,12 0 0 0 112,262 L112,126 A12,12 0 0 0 124,114 Z"
            fill="url(#plaque-fill)" stroke="url(#gold-edge)" stroke-width="3"
            style="filter: drop-shadow(0 3px 5px rgba(0,0,0,0.45));"/>
    </svg>

    <p class="plaque-text line-host">The Copperfield Lodge Hotel</p>
    <p class="plaque-text line-welcomes">Welcomes</p>
    <p class="plaque-text line-headline">2019 International Delegates</p>
    <p class="plaque-text line-place">To The Hudson Valley</p>
    <p class="plaque-text line-state">In New York</p>
    <p class="plaque-text line-hashtag">#copperfieldlodgehotel</p>
  </section>
</main>
</body>
</html>
```